Business Cards for Marco and Tobin

Design of business cards for two people with the recently created brand Valcor Mobile. Valcor Mobile wants to become a worldwide major player on the secondhand phone market. It gathers send hand phones from individuals, refurbish them and sell them throughout the world. It has a green impact (recycling) and we also contribute to social project in Africa (a percentage of our benefits are sent to build school, sport facilities, etc.

Target Market(s)

B2B - Marco and Tobin are in contact with distributors across Africa.

Industry/Entity Type

Wireless Communication

Contact Information for Business Card

Marco Feuillet
Head of Emerging Markets
Valcor Energy South Africa (Pty) Ltd
Kestrel Road 47
2031 Sandton - Johannesburg
South Africa
Tel: + 27 10 555 0148
Mobile : +27 82 55 104
Email : marco.feuillet@valcormobile.example
Skype: marco.feuillet
Web: www.valcormobile.example
 

Tobin Farrow
Head of Southern Africa
Kestrel Road 47
South Africa
Tel: + 27 10 555 0148
Mobile: +27 83 555 0276
Email: tobin.farrow@valcormobile.example
Skype: tobin.farrow
Web: www.valcormobile.example

Requirements
Must have
• The cards need to be "serious", trustable, with a worldwide presence.
Nice to have
• Some "green" / recycling touch would be nice but not necessary if in contradiction with the general design.

```html
<!DOCTYPE html>
<html lang="en">
<head>
<meta charset="utf-8">
<title>Valcor Mobile – Business Card</title>
<link rel="stylesheet" href="https://fonts.googleapis.com/css2?family=Open+Sans:wght@400;600;700&display=swap">
<style>
  :root {
    --backdrop: #e9e9e6;
    --card-white: #f6f6f6;
    --navy: #0d2a45;
    --brand-blue: #2b96d6;
    --text-grey: #4a4a4a;
    --rule-grey: #9a9a9a;
  }
  * { margin: 0; padding: 0; box-sizing: border-box; }
  html, body { width: 1200px; height: 960px; overflow: hidden; }
  body {
    position: relative;
    background: var(--backdrop);
    font-family: "Open Sans", Arial, sans-serif;
  }
  .card {
    position: absolute;
    width: 600px;
    height: 343px;
    overflow: hidden;
  }
  .card-front { left: 314px; top: 113px; background: var(--card-white); }
  .card-back { left: 311px; top: 472px; background: var(--brand-blue); }

  .brand-name {
    position: absolute;
    font-weight: 700;
    white-space: nowrap;
    letter-spacing: -0.5px;
  }
  .card-front .brand-name {
    right: 31px; top: 118px;
    font-size: 29px;
    color: var(--navy);
  }
  .card-back .brand-name {
    left: 0; right: 0; top: 212px;
    text-align: center;
    font-size: 33px;
    color: #ffffff;
  }

  .person { position: absolute; left: 28px; top: 162px; }
  .person-name {
    font-size: 19px; font-weight: 700; color: var(--navy);
    letter-spacing: 0.2px; line-height: 24px;
  }
  .person-role { font-size: 15px; color: var(--brand-blue); line-height: 20px; }

  .divider {
    position: absolute; left: 28px; top: 211px;
    width: 541px; height: 1px; background: var(--rule-grey);
  }

  .contact-list {
    position: absolute; left: 27px; top: 225px;
    list-style: none; font-size: 13.5px; color: var(--text-grey);
  }
  .contact-list li { display: flex; align-items: center; height: 19px; }
  .contact-list svg { width: 14px; height: 14px; margin-right: 8px; fill: var(--navy); flex: none; }

  .address {
    position: absolute; right: 31px; top: 228px;
    text-align: right; font-size: 13.5px; line-height: 19.5px; color: var(--text-grey);
    font-style: normal;
  }

  .wave { position: absolute; left: 0; bottom: 0; width: 600px; height: 343px; }

  .web-address {
    position: absolute; left: 0; right: 0; top: 290px;
    text-align: center; color: #ffffff;
    font-size: 14px; letter-spacing: 5px;
  }
</style>
</head>
<body>

<section class="card card-front">
  <div class="brand-name">Valcor Mobile</div>

  <div class="person">
    <div class="person-name">MARCO FEUILLET</div>
    <div class="person-role">Head of Emerging Markets</div>
  </div>

  <div class="divider"></div>

  <ul class="contact-list">
    <li>
      <svg viewBox="0 0 14 14" aria-hidden="true"><path d="M1 4c0-2 3-3 6-3s6 1 6 3v1.5h-3V4H4v1.5H1z M3 7h8l1 6H2z"/></svg>
      + 27 10 555 0148
    </li>
    <li>
      <svg viewBox="0 0 14 14" aria-hidden="true"><path d="M4 0h6a1 1 0 0 1 1 1v12a1 1 0 0 1-1 1H4a1 1 0 0 1-1-1V1a1 1 0 0 1 1-1zm1 2v8h4V2zm2 9a1 1 0 1 0 0 2a1 1 0 0 0 0-2z"/></svg>
      +27 82 55 104
    </li>
    <li>
      <svg viewBox="0 0 14 14" aria-hidden="true"><path d="M1 3h12v1L7 8 1 4z M1 5.5l6 4 6-4V11H1z"/></svg>
      marco.feuillet@valcormobile.example
    </li>
    <li>
      <svg viewBox="0 0 14 14" aria-hidden="true"><circle cx="7" cy="7" r="6"/></svg>
      marco.feuillet
    </li>
  </ul>

  <address class="address">
    Valcor Energy South Africa (Pty) Ltd<br>
    Kestrel Road 47<br>
    2031 Sandton - Johannesburg<br>
    South Africa
  </address>

  <svg class="wave" viewBox="0 0 600 343" aria-hidden="true">
    <path d="M0 286 C70 318 160 330 270 322 C390 313 480 300 600 326 L600 343 L0 343 Z" fill="var(--brand-blue)"/>
    <path d="M0 312 C90 334 200 339 300 327 C400 315 500 311 600 331 L600 343 L0 343 Z" fill="#ffffff"/>
    <path d="M0 316 C90 338 200 343 300 331 C400 319 500 315 600 335 L600 343 L0 343 Z" fill="var(--navy)"/>
  </svg>
</section>

<section class="card card-back">
  <div class="brand-name">Valcor Mobile</div>
  <div class="web-address">www.valcormobile.example</div>
</section>

</body>
</html>
```